Quiet ridge balance Business cards - yoga studio

We need business cards for our yoga studio Quietridge Balance.
We would like to see designs that include the colour blue and our logo.
The business card should communicate a feeling of strength and calm

Industry/Entity Type

Business

Requirements
Must have
• The business card must include
"Helena Moorcroft - Director"
and
"27 Tamarind Crescent
Fernleigh
VIC 3911
Ph - 0451 806 214"

```html
<!DOCTYPE html>
<html lang="en">
<head>
<meta charset="utf-8">
<title>Quietridge Balance — Business Card</title>
<link rel="stylesheet" href="https://fonts.googleapis.com/css2?family=Questrial&display=swap">
<style>
  :root {
    --teal: #67b6c9;
    --teal-light: #b3d8e1;
    --paper: #ffffff;
  }
  html, body {
    margin: 0;
    padding: 0;
    overflow: hidden;
    background: var(--paper);
  }
  .card {
    position: relative;
    width: 1200px;
    height: 720px;
    background: var(--paper);
    overflow: hidden;
    font-family: "Questrial", "Century Gothic", sans-serif;
    color: var(--teal);
  }
  .brand {
    position: absolute;
    left: 60px;
    top: 105px;
    width: 420px;
    text-align: center;
  }
  .brand-mark {
    display: block;
    width: 170px;
    height: 170px;
    margin: 0 auto 58px;
    border-radius: 50%;
    background: var(--teal);
  }
  .brand-name {
    margin: 0;
    font-size: 42px;
    font-weight: 400;
    letter-spacing: 1px;
    white-space: nowrap;
  }
  .person {
    position: absolute;
    right: 80px;
    top: 314px;
    text-align: right;
  }
  .person-name {
    margin: 0;
    font-size: 51px;
    font-weight: 400;
    letter-spacing: 2px;
    line-height: 1;
  }
  .person-role {
    margin: 20px 0 0;
    font-size: 22px;
    font-weight: 400;
    letter-spacing: 4px;
    text-transform: uppercase;
  }
  .bands {
    position: absolute;
    left: 0;
    top: 0;
  }
  .band-light { fill: var(--teal-light); }
  .band-dark { fill: var(--teal); }
  .contact {
    position: absolute;
    right: 82px;
    top: 540px;
    text-align: right;
    color: var(--paper);
    font-size: 29px;
    line-height: 43px;
    letter-spacing: 0.5px;
    white-space: nowrap;
  }
  .contact p { margin: 0; }
</style>
</head>
<body>
  <div class="card">
    <div class="brand">
      <span class="brand-mark" aria-hidden="true"></span>
      <p class="brand-name">Quietridge Balance</p>
    </div>

    <div class="person">
      <h1 class="person-name">Helena Moorcroft</h1>
      <p class="person-role">Director</p>
    </div>

    <svg class="bands" width="1200" height="720" viewBox="0 0 1200 720" aria-hidden="true">
      <polygon class="band-light" points="8,555 478,555 430,648 8,648"/>
      <polygon class="band-dark" points="508,518 1187,518 1187,648 436,648"/>
    </svg>

    <div class="contact">
      <p>27 Tamarind Crescent, Fernleigh, VIC 3911</p>
      <p>Phone&nbsp; 0451 806 214</p>
    </div>
  </div>
</body>
</html>
```